New Australian Beverage Company Needs a Bottle Label Design

We are after a bottle label design for our new aloe vera drinks called 'Sun Ridge'.

There are 5+ different colourrs we would like to compliment the flavors.

We are after a logo that is simple and eye catching.
Updates

Project Deadline Extended Reason: Business partner is currently overseas and would like to review all designs with him upon his return. Added Thursday, May 14, 2015

Project Deadline Extended Reason: We have received a number of great designs and we require more time to decide which direction we would like to take our label design. Thank you for your understanding. Added Thursday, May 21, 2015

Target Market(s)

Our target market is open for all as we would like to supply our drinks to quench everyone's thirst, however our biggest customers would be the teenagers to adults up to around the age of 50.

Industry/Entity Type

It Company

Requirements
Must have
• We are after a refreshing label that catches the eyes and makes you feel like picking it up and drinking it.

```html
<!DOCTYPE html>
<html lang="en">
<head>
<meta charset="utf-8">
<title>Sun Ridge – Bottle Labels</title>
<link href="https://fonts.googleapis.com/css2?family=Cinzel:wght@400&family=Gochi+Hand&display=swap" rel="stylesheet">
<style>
  :root {
    --page: #f4f6f1;
    --white: #ffffff;
    --raspberry: #de1f48;
    --orange: #f9b52b;
    --sky: #42a6dc;
    --leaf-light: #d8e3cc;
    --leaf-dark: #8fae74;
    --ice: #e4e7ea;
  }
  * { box-sizing: border-box; margin: 0; padding: 0; }
  html, body {
    width: 1200px;
    height: 1034px;
    overflow: hidden;
    background: var(--page);
  }
  .label-range {
    position: absolute;
    inset: 0;
    display: flex;
    justify-content: center;
    align-items: center;
    gap: 40px;
  }
  .label {
    --tone: var(--orange);
    position: relative;
    width: 340px;
    height: 460px;
    background: var(--white);
    box-shadow: 0 6px 24px rgba(0,0,0,0.08);
    overflow: hidden;
  }
  .label--raspberry { --tone: var(--raspberry); }
  .label--orange { --tone: var(--orange); }
  .label--sky { --tone: var(--sky); }

  .label__band {
    position: absolute;
    left: 0;
    width: 100%;
    display: block;
  }
  .label__band path { fill: var(--tone); }
  .label__band--top { top: 0; height: 150px; }
  .label__band--bottom { bottom: 0; height: 110px; }

  .brand-name {
    position: absolute;
    top: 30px;
    left: 0;
    width: 100%;
    text-align: center;
    font-family: "Cinzel", serif;
    font-weight: 400;
    font-size: 40px;
    line-height: 1.05;
    color: var(--white);
    letter-spacing: 1px;
  }
  .flavour {
    position: absolute;
    top: 158px;
    left: 0;
    width: 100%;
    text-align: center;
    font-family: "Gochi Hand", cursive;
    font-size: 34px;
    color: var(--tone);
    transform: rotate(3deg);
  }
  .flavour-art {
    position: absolute;
    top: 212px;
    left: 95px;
    width: 150px;
    height: 140px;
    border-radius: 12px;
    background: linear-gradient(135deg, var(--ice) 0%, var(--ice) 45%, var(--leaf-light) 60%, var(--leaf-dark) 100%);
  }
  .volume {
    position: absolute;
    bottom: 40px;
    left: 0;
    width: 100%;
    text-align: center;
    font-family: "Cinzel", serif;
    font-size: 20px;
    color: var(--white);
  }
</style>
</head>
<body>
<main class="label-range">

  <section class="label label--raspberry">
    <svg class="label__band label__band--top" viewBox="0 0 340 150" preserveAspectRatio="none" aria-hidden="true">
      <path d="M0 0 H340 V138 C260 112 180 150 90 136 C50 130 20 124 0 128 Z"/>
    </svg>
    <h2 class="brand-name">Sun<br>Ridge</h2>
    <p class="flavour">raspberry flavour</p>
    <div class="flavour-art" role="img" aria-label="Ice cubes with fresh green tea leaves"></div>
    <svg class="label__band label__band--bottom" viewBox="0 0 340 110" preserveAspectRatio="none" aria-hidden="true">
      <path d="M0 22 C80 4 160 30 240 14 C290 4 320 8 340 16 V110 H0 Z"/>
    </svg>
    <p class="volume">500ml</p>
  </section>

  <section class="label label--orange">
    <svg class="label__band label__band--top" viewBox="0 0 340 150" preserveAspectRatio="none" aria-hidden="true">
      <path d="M0 0 H340 V138 C260 112 180 150 90 136 C50 130 20 124 0 128 Z"/>
    </svg>
    <h2 class="brand-name">Sun<br>Ridge</h2>
    <p class="flavour">orange flavour</p>
    <div class="flavour-art" role="img" aria-label="Ice cubes with fresh green tea leaves"></div>
    <svg class="label__band label__band--bottom" viewBox="0 0 340 110" preserveAspectRatio="none" aria-hidden="true">
      <path d="M0 22 C80 4 160 30 240 14 C290 4 320 8 340 16 V110 H0 Z"/>
    </svg>
    <p class="volume">500ml</p>
  </section>

  <section class="label label--sky">
    <svg class="label__band label__band--top" viewBox="0 0 340 150" preserveAspectRatio="none" aria-hidden="true">
      <path d="M0 0 H340 V138 C260 112 180 150 90 136 C50 130 20 124 0 128 Z"/>
    </svg>
    <h2 class="brand-name">Sun<br>Ridge</h2>
    <p class="flavour">orange flavour</p>
    <div class="flavour-art" role="img" aria-label="Ice cubes with fresh green tea leaves"></div>
    <svg class="label__band label__band--bottom" viewBox="0 0 340 110" preserveAspectRatio="none" aria-hidden="true">
      <path d="M0 22 C80 4 160 30 240 14 C290 4 320 8 340 16 V110 H0 Z"/>
    </svg>
    <p class="volume">500ml</p>
  </section>

</main>
</body>
</html>
```